Women's Empowerment & Prayer Brunch - Matching Poster, flyer and Postcard

We are a Christian Event & Travel Company and we are hosting our inaugural event on June 10, 2017. This event is a women's empowerment & prayer brunch aboard a private yacht leaving out of Larkspur Landing, Maryland. The event will cater to women who have a vision to start or have already embarked on the journey of starting or growing a business or ministry. The event calls for a matching poster, flyer and postcard design that give an elegant & exquisite feel with just the right breath of freshness. The colors should reflect our logo as this is our launch event. I have also included 2 photos of the Coralwind Heritage Village production (one of our sponsors) - Please include but do not make it take over the design - this is to advertise the door prize. The final design will portray the branding of the company (Christian, travel, events, elegance, professional), the branding of the event (elegant and luxurious) and the importance of this launch event.
Please include the following information:
Brightwell Event & Travel Group presents
Event name: Climbing the Hill: Trust, Service & Devotion.
Tag Line/Description: An Exquisite Women's Empowerment & Prayer Brunch.
Guest Speaker: Minister Harriet L. Dunmore (Photo included)
VP of TrustLine
Asst. Pastor & First Lady of Gilead Baptist Church
Special Guest Psalmist: Minister Tessa Holbrook (Photo Included)
Worship Director of Stonefield Community Church
Vocalist, Songwriter, Musician, and Clinician
Venue: Aboard the Regal Tide Yacht
Dock: Larkspur Landing
342 Marlow Court, Oxen Hill, MD 20712
Boarding 10:00am
Sailing Promptly at 10:30am
(Please be on time the yacht will not wait)
Date: Saturday June 10, 2017
Tickets: Early Bird US$75.00/person (ends May 15, 2017)
Regular Tickets US$95.99
Purchase Tickets at www.brightwellevent-travel.example/climbing-the-hill
SPACE IS LIMITED DUE TO YACHT CAPACITY
Grand Prize: Julian Ardent Purse
Door Prize: 2 Tickets to the Islander Coralwind Heritage Village
Other prizes for special ladies in attendance.
Ladies are asked to dress in Elegant White Ensemble
Corporate Sponsors:
The Coralwind Heritage Village (Logo included)
R. Lanning Photography (Logo included)
Special Thanks to our Individual Sponsors:
Mrs. G. Whitlow, Mr. K Prentice & Mr. S. Dorsey

Target Market(s)

Women, Business, Ministry, Christians, Middle to Upper Class

Industry/Entity Type

Events

Font styles to use
Serif
Script

Requirements
Must have
• Elegance, professional, vivid in color & font. be creative in Visual and FONT!
• Poster: 18" X 24"
• Flyer: one sided.
• ***** the final design chosen will have a cross referenced design of 1 flyer, 1 postcard 1 poster. This was included so you have a reference - Be creative!!!!!!
Nice to have
• Matching across all 3 designs (poster, flyer & postcard) but sized appropriately and just enough difference to play up the design and be appealing.
• I uploaded 3 example flyers to give you inspiration of the type of visuals I'm looking for. I removed my amateur sample because the designs were copying it instead of being creative.
Should not have
• Any thing inappropriate, alcohol oriented or sexual

```html
<!DOCTYPE html>
<html lang="en">
<head>
<meta charset="utf-8">
<title>Climbing the Hill – Women's Empowerment &amp; Prayer Brunch</title>
<link rel="stylesheet" href="https://fonts.googleapis.com/css2?family=Ultra&family=Oswald:wght@500;700&family=Cinzel+Decorative:wght@400;700&family=Cabin:wght@400;600&family=Caveat:wght@500;700&family=Crimson+Text:wght@400;700&family=Cinzel:wght@600&display=swap">
<style>
  :root{
    --navy:#28336b;
    --night:#0b0d16;
    --gold:#e6dd45;
    --gold-soft:#e9dd7a;
    --ink:#111;
    --white:#f4f4f4;
    --sponsor-grey:#e4e4e4;
  }
  *{margin:0;padding:0;box-sizing:border-box}
  html,body{width:900px;height:1200px;overflow:hidden;background:var(--navy)}
  .poster{position:relative;width:900px;height:1200px;background:var(--navy);overflow:hidden;font-family:'Crimson Text',serif;color:var(--white)}
  .abs{position:absolute}
  .center{left:0;width:900px;text-align:center}

  .ribbon{position:absolute;left:0;top:0}
  .brand{top:52px;display:flex;align-items:center;justify-content:center;gap:12px;font-family:'Cinzel',serif;font-weight:600;font-size:28px;color:var(--gold);letter-spacing:1px}
  .brand-dot{width:14px;height:14px;border-radius:50%;background:var(--gold)}
  .brand-sub{top:96px;font-family:'Cinzel',serif;font-weight:600;font-size:15px;letter-spacing:4px;color:var(--gold)}

  .scene{left:0;top:178px;width:900px;height:737px;background:
    radial-gradient(ellipse 380px 260px at 50% 22%,rgba(130,140,200,.55),transparent 70%),
    linear-gradient(180deg,#141622 0%,#3a4068 30%,#2b2f4c 55%,#10121c 80%,#07080d 100%)}

  .presents{top:184px;font-family:'Oswald',sans-serif;font-weight:700;font-size:21px;color:var(--gold)}
  .title{top:212px;font-family:'Ultra',serif;font-size:56px;color:var(--gold);letter-spacing:2px}
  .virtues{top:276px;font-family:'Oswald',sans-serif;font-weight:700;font-size:26px;color:var(--gold)}
  .tagline{top:321px;font-family:'Cinzel Decorative',serif;font-size:23px;line-height:29px;color:var(--gold-soft)}
  .aboard{top:384px;font-family:'Cinzel Decorative',serif;font-size:17px;color:var(--gold-soft)}
  .venue{top:418px;font-family:'Cabin',sans-serif;font-size:26px;color:var(--gold-soft)}
  .dock{top:458px;font-family:'Cabin',sans-serif;font-size:20px;color:var(--gold-soft)}
  .address{top:492px;font-family:'Cabin',sans-serif;font-size:18px;color:var(--white)}
  .boarding{top:527px;font-family:'Cabin',sans-serif;font-weight:600;font-size:23px;line-height:30px;color:var(--gold-soft)}
  .note{top:594px;font-family:'Cabin',sans-serif;font-weight:600;font-size:14px;color:var(--white)}

  .date{left:305px;top:630px;width:290px;height:35px;background:var(--gold);border-radius:7px;font-family:'Oswald',sans-serif;font-weight:700;font-size:23px;line-height:35px;text-align:center;color:var(--ink);word-spacing:8px}
  .early{top:672px;font-family:'Caveat',cursive;font-weight:500;font-size:32px;color:var(--gold-soft)}
  .early-ends{top:704px;font-family:'Caveat',cursive;font-size:18px;color:var(--gold-soft)}
  .regular{top:724px;font-family:'Caveat',cursive;font-weight:500;font-size:32px;color:var(--gold-soft)}

  .purchase{left:222px;top:765px;width:469px;height:45px;background:var(--navy);border-radius:8px;text-align:center;padding-top:3px}
  .purchase-url{font-family:'Oswald',sans-serif;font-weight:500;font-size:14.5px;color:var(--gold-soft)}
  .purchase-note{font-family:'Caveat',cursive;font-size:14px;color:var(--gold-soft);letter-spacing:.5px}

  .prizes{top:832px;font-family:'Crimson Text',serif;font-size:13.5px;line-height:25.5px;color:var(--gold-soft);text-transform:uppercase}

  .photo{border:2px solid #0a0a0a}
  .speaker-photo{left:54px;top:409px;width:151px;height:182px;background:linear-gradient(135deg,#8c5a48,#b8373c 60%,#5a2a2a)}
  .psalmist-photo{left:696px;top:409px;width:151px;height:186px;background:linear-gradient(160deg,#2c3a5a,#1a2236 60%,#d8d4cc)}
  .dance-photo{left:25px;top:712px;width:183px;height:121px;background:linear-gradient(180deg,#3b2a1e,#7a5a32 55%,#3d4a1e)}
  .fire-photo{left:699px;top:715px;width:180px;height:118px;background:radial-gradient(ellipse 70px 40px at 50% 50%,#d8892c,#3a2410 70%,#141414)}

  .caption{font-family:'Crimson Text',serif;font-size:13px;line-height:16.5px;text-align:center;color:var(--white)}
  .caption strong{color:var(--white)}
  .speaker-caption{left:29px;top:600px;width:200px}
  .psalmist-caption{left:660px;top:602px;width:220px}

  .dress{top:926px;font-family:'Crimson Text',serif;font-size:22px;color:var(--gold-soft)}
  .on-sale{left:292px;top:961px;width:344px;height:35px;background:#050505;border-radius:18px;font-family:'Oswald',sans-serif;font-weight:500;font-size:22px;line-height:35px;text-align:center;color:var(--gold-soft);word-spacing:6px}
  .sponsors-bar{left:285px;top:1010px;width:360px;height:29px;background:var(--gold);border-radius:3px;font-family:'Oswald',sans-serif;font-weight:700;font-size:23px;line-height:29px;letter-spacing:4px;text-align:center;color:var(--navy)}
  .sponsor{top:1045px;height:107px;border-radius:4px;display:flex;align-items:center;justify-content:center;text-align:center;font-family:'Crimson Text',serif;color:#333}
  .sponsor-photo{left:284px;width:115px;background:var(--sponsor-grey);font-size:13px;line-height:16px}
  .sponsor-village{left:409px;width:236px;background:#fff;font-size:21px;font-weight:700;line-height:24px;color:#2a3f7a}
  .thanks{top:1160px;font-family:'Crimson Text',serif;font-size:21px;color:var(--gold-soft)}
</style>
</head>
<body>
<main class="poster">
  <div class="abs scene" role="img" aria-label="Moonlit lake with a long wooden dock under a cloudy night sky"></div>

  <svg class="ribbon" width="200" height="200" viewBox="0 0 200 200" aria-hidden="false">
    <polygon points="0,140 140,0 186,0 0,186" fill="var(--gold)"/>
    <text x="82" y="90" transform="rotate(-45 82 90)" text-anchor="middle" font-family="Crimson Text, serif" font-weight="700" font-size="19" fill="var(--navy)">Limited Tickets</text>
  </svg>

  <div class="abs center brand"><span class="brand-dot"></span>Brightwell</div>
  <div class="abs center brand-sub">EVENT &amp; TRAVEL GROUP</div>

  <div class="abs center presents">Presents</div>
  <h1 class="abs center title">CLIMBING THE HILL</h1>
  <div class="abs center virtues">TRUST ~ SERVICE~DEVOTION</div>
  <div class="abs center tagline">An Executive Women’s Empowerment<br>&amp; Prayer Brunch</div>
  <div class="abs center aboard">aboard</div>

  <div class="abs center venue">Venue : Aboard the Regal Tide Yacht</div>
  <div class="abs center dock">DOCK : LARKSPUR LANDING</div>
  <div class="abs center address">342 Marlow Court, Oxen Hill , MD 20712</div>
  <div class="abs center boarding">Boarding: 10:00 am<br>Sailing Promptly at: 10:30 am</div>
  <div class="abs center note">(Please be on time the yacht will not wait)</div>

  <div class="abs date">Saturday 10th June 2017</div>
  <div class="abs center early">Early Bird: $75 /Person</div>
  <div class="abs center early-ends">Early Birds ends 15th May 2017</div>
  <div class="abs center regular">Regular Tickets: $95.99 /Person</div>

  <div class="abs purchase">
    <div class="purchase-url">Purchase Tickets at www.brightwellevent-travel.example/climbing-the-hill</div>
    <div class="purchase-note">SPACE IS LIMITED DUE TO YACHT CAPACITY</div>
  </div>

  <div class="abs center prizes">
    Grand Prize : Julian Ardent Purse<br>
    Door Prize : 2 Tickets to the Coralwind Heritage Village in Hawaii<br>
    Other Prizes for Special Ladies in Attendance
  </div>

  <div class="abs photo speaker-photo" role="img" aria-label="Portrait photo of guest speaker Harriet L. Dunmore"></div>
  <div class="abs caption speaker-caption">Guest Speaker<br><strong>Mstr. Harriet L. Dunmore</strong><br>Lady &amp; Asst Pastor Gilead<br>Baptist Church<br>Vice-President of TrustLine</div>

  <div class="abs photo psalmist-photo" role="img" aria-label="Portrait photo of psalmist Tessa Holbrook"></div>
  <div class="abs caption psalmist-caption">Special Guest Psalmist<br><strong>Mstr. Tessa Holbrook</strong><br>Worship Director of Stonefield<br>Community Church<br>Vocalist, Songwriter, Musician<br>and Clinician</div>

  <div class="abs dance-photo" role="img" aria-label="Photo of island dancers performing on stage at the heritage village"></div>
  <div class="abs fire-photo" role="img" aria-label="Photo of fire dancers spinning flames at night"></div>

  <div class="abs center dress">Ladies are asked to dress in Elegant White Ensembles</div>
  <div class="abs on-sale">Tickets on Sale 18th March 2017</div>
  <div class="abs sponsors-bar">CORPORATE SPONSORS</div>
  <div class="abs sponsor sponsor-photo">R. Lanning<br>Photography</div>
  <div class="abs sponsor sponsor-village">Coralwind<br>Heritage Village</div>
  <div class="abs center thanks">Special Thanks to our Individual Sponsors: Mrs. G. Whitlow, Mr. K Prentice &amp; Mr. S. Dorsey</div>
</main>
</body>
</html>
```